Building company business card

Design and print business cards for BRENTHOLM PTY LTD.
A residantial homes building company.
Mark Lantern already designed the company Logo.

```html
<!DOCTYPE html>
<html lang="en">
<head>
<meta charset="utf-8">
<title>Brentholm Pty Ltd – Business Card</title>
<link rel="stylesheet" href="https://fonts.googleapis.com/css2?family=Lato:wght@400;700;900&display=swap">
<style>
  :root {
    --navy: #141b52;
    --navy-deep: #0a0e38;
    --gold: #c8963a;
    --gold-light: #e2b95e;
    --paper: #f7f7f7;
    --ink: #2c2f3a;
    --backdrop: #5c5f63;
  }
  * { box-sizing: border-box; margin: 0; padding: 0; }
  html, body {
    width: 1200px; height: 900px; overflow: hidden;
    background: var(--backdrop);
    font-family: "Lato", sans-serif;
  }
  .canvas { position: relative; width: 1200px; height: 900px; }
  .card {
    position: absolute; left: 273px; width: 654px; height: 400px;
    overflow: hidden; box-shadow: 0 10px 24px rgba(0,0,0,.35);
    background: var(--paper);
  }
  .card--front { top: 34px; }
  .card--back  { top: 466px; }
  .card__art { position: absolute; inset: 0; width: 100%; height: 100%; }

  .wordmark {
    position: absolute; color: var(--navy); font-weight: 900;
    letter-spacing: 1px; line-height: 1; white-space: nowrap;
  }
  .card--front .wordmark { left: 150px; top: 246px; font-size: 54px; }
  .wordmark__suffix {
    display: block; text-align: right; font-size: 17px;
    letter-spacing: .5px; margin-bottom: 6px;
  }

  .holder { position: absolute; left: 36px; top: 120px; color: #fff; }
  .holder__name {
    color: var(--gold-light); font-weight: 700; font-size: 16px;
    letter-spacing: 1px; text-transform: uppercase; white-space: nowrap;
  }
  .holder__role { font-size: 15px; margin: 2px 0 14px; }
  .holder__phone { display: flex; align-items: center; gap: 6px; font-size: 17px; margin-bottom: 4px; }
  .icon { width: 12px; height: 16px; flex: none; }

  .contacts {
    position: absolute; right: 194px; top: 196px; text-align: right;
    color: var(--ink); font-size: 14px; line-height: 1.45; white-space: nowrap;
  }
  .contacts__row { display: flex; align-items: center; justify-content: flex-end; gap: 6px; }
  .contacts__address { margin-top: 6px; padding-right: 18px; }
  .divider {
    position: absolute; left: 470px; top: 188px; width: 1px; height: 124px;
    background: var(--navy); opacity: .6;
  }
  .card--back .wordmark {
    left: 482px; top: 240px; font-size: 19px; display: flex; align-items: center; gap: 6px;
  }
  .wordmark__square { width: 12px; height: 12px; background: var(--gold); flex: none; }

  .legal {
    position: absolute; right: 184px; top: 322px; text-align: right;
    color: var(--navy); font-size: 14px; line-height: 1.45; white-space: nowrap;
  }
  .legal__rule {
    position: absolute; left: 210px; right: 184px; top: 316px; height: 1px;
    background: var(--gold); opacity: .6;
  }
</style>
</head>
<body>
<main class="canvas">

  <section class="card card--front" aria-label="Card front">
    <svg class="card__art" viewBox="0 0 654 400" preserveAspectRatio="none" aria-hidden="true">
      <defs>
        <linearGradient id="navyFront" x1="0" y1="0" x2="1" y2="1">
          <stop offset="0" stop-color="#1a2260"/><stop offset="1" stop-color="#0a0e38"/>
        </linearGradient>
        <linearGradient id="goldFront" x1="0" y1="0" x2="1" y2="0">
          <stop offset="0" stop-color="#d6aa4d"/><stop offset="1" stop-color="#b8822c"/>
        </linearGradient>
      </defs>
      <rect width="654" height="400" fill="url(#navyFront)"/>
      <polygon points="0,128 276,18 654,226 654,400 0,400" fill="#070a2c"/>
      <polygon points="0,146 288,30 654,238 654,400 0,400" fill="url(#goldFront)"/>
      <polygon points="0,224 326,82 654,300 654,400 0,400" fill="#f4f4f4"/>
    </svg>
    <div class="wordmark"><span class="wordmark__suffix">Pty Ltd</span>BRENTHOLM</div>
  </section>

  <section class="card card--back" aria-label="Card back">
    <svg class="card__art" viewBox="0 0 654 400" preserveAspectRatio="none" aria-hidden="true">
      <defs>
        <linearGradient id="navyBack" x1="0" y1="0" x2="1" y2="1">
          <stop offset="0" stop-color="#1a2260"/><stop offset="1" stop-color="#0a0e38"/>
        </linearGradient>
        <linearGradient id="goldBack" x1="0" y1="1" x2="1" y2="0">
          <stop offset="0" stop-color="#b8822c"/><stop offset="1" stop-color="#e6bd62"/>
        </linearGradient>
      </defs>
      <rect width="654" height="400" fill="url(#navyBack)"/>
      <polygon points="60,400 340,38 654,40 654,400" fill="#070a2c"/>
      <polygon points="74,400 352,48 654,50 654,400" fill="url(#goldBack)"/>
      <polygon points="120,400 400,100 654,110 654,400" fill="#f4f4f4"/>
    </svg>

    <div class="holder">
      <p class="holder__name">Dorian (Dee) Castell</p>
      <p class="holder__role">Director</p>
      <p class="holder__phone">
        <svg class="icon" viewBox="0 0 12 16" aria-hidden="true"><rect x="1" y="1" width="10" height="14" rx="2" fill="none" stroke="#c8963a" stroke-width="1.4"/><circle cx="6" cy="12.5" r=".9" fill="#c8963a"/></svg>
        0412 583 207
      </p>
      <p class="holder__phone">
        <svg class="icon" viewBox="0 0 12 16" aria-hidden="true"><rect x="1" y="1" width="10" height="14" rx="2" fill="none" stroke="#c8963a" stroke-width="1.4"/><circle cx="6" cy="12.5" r=".9" fill="#c8963a"/></svg>
        0438 116 940
      </p>
    </div>

    <div class="contacts">
      <p class="contacts__row">0412 583 207
        <svg class="icon" viewBox="0 0 12 16" aria-hidden="true"><path d="M2 5c1-2 7-2 8 0l-1 2H3z M3 8h6v5H3z" fill="#c8963a"/></svg>
      </p>
      <p class="contacts__row">dee@brentholm-bh.com
        <svg class="icon" viewBox="0 0 12 16" aria-hidden="true"><rect x="1" y="4" width="10" height="8" fill="#c8963a"/><path d="M1 4l5 4 5-4" fill="none" stroke="#fff" stroke-width="1"/></svg>
      </p>
      <p class="contacts__address">PO Box 248<br>Kelmore East Vic 3187</p>
    </div>
    <div class="divider"></div>
    <div class="wordmark"><span class="wordmark__square"></span>BRENTHOLM</div>

    <div class="legal__rule"></div>
    <div class="legal">
      <p>Brentholm Pty Ltd</p>
      <p>ABN - 48 215 906 372 | CDB-U 51846</p>
    </div>
  </section>

</main>
</body>
</html>
```